Biz Card for Harrowfield Property Partners - HWPP

Harrowfield Property Partners is a commercial real estate acquisitions firm. We buy commercial property and need to raise capital from investors for each deal we buy. The vibe needs to be: give us your money, we will multiply it.
Our website: www.hrwpp-example.com
Competitors are: https://velmarholdings-example.com/, https://tribanquepartners-example.com/, http://www.ostrellecapital-example.com/
Target Market(s)
High Net Worth Individuals, Bankers, Insurance Companies, Commercial Real Estate Brokers.
Industry/Entity Type
Investment Banking
Contact Information for Business Card
Name, Title, Addess, Cell#, Office#, email, website
Requirements
Must have
- use one of our logos. See website for look and feel: www.hrwpp-example.com
Nice to have
- see website: www.hrwpp-example.com

```html
<!DOCTYPE html>
<html lang="en">
<head>
<meta charset="utf-8">
<title>Harrowfield Property Partners – Business Card</title>
<link rel="stylesheet" href="https://fonts.googleapis.com/css2?family=Roboto:wght@300;400;500;700&display=swap">
<style>
  :root {
    --navy: #0b2a45;
    --white: #ffffff;
    --ink: #0b2a45;
    --muted: #3c4f63;
    --rule: #55677a;
    --stage: #d9dcdf;
  }
  * { box-sizing: border-box; margin: 0; padding: 0; }
  html, body { width: 1200px; height: 800px; overflow: hidden; }
  body {
    background: var(--stage);
    font-family: "Roboto", Arial, sans-serif;
    display: flex;
    flex-direction: column;
    align-items: center;
    justify-content: center;
    gap: 40px;
  }
  .card {
    width: 560px;
    height: 320px;
    position: relative;
    box-shadow: 0 6px 18px rgba(0,0,0,0.18);
  }

  /* Front */
  .card-front {
    background: var(--navy);
    color: var(--white);
    display: flex;
    flex-direction: column;
    align-items: center;
    justify-content: center;
  }
  .brand-mark {
    width: 92px;
    height: 92px;
    border-radius: 50%;
    background: var(--white);
    margin-bottom: 22px;
  }
  .brand-name {
    font-weight: 400;
    font-size: 19px;
    letter-spacing: 0.32em;
    text-transform: uppercase;
    color: var(--white);
    margin-left: 0.32em;
  }
  .front-web {
    margin-top: 30px;
    font-size: 13px;
    font-weight: 300;
    letter-spacing: 0.04em;
  }

  /* Back */
  .card-back {
    background: var(--white);
    border-bottom: 5px solid var(--navy);
    color: var(--ink);
  }
  .back-logo {
    position: absolute;
    left: 88px;
    top: 70px;
    width: 130px;
    display: flex;
    flex-direction: column;
    align-items: center;
  }
  .back-logo .brand-mark {
    width: 116px;
    height: 116px;
    background: var(--navy);
    margin-bottom: 10px;
  }
  .back-logo .brand-name {
    font-size: 8px;
    letter-spacing: 0.18em;
    color: var(--navy);
    margin-left: 0;
    white-space: nowrap;
  }
  .divider {
    position: absolute;
    left: 262px;
    top: 62px;
    width: 1px;
    height: 112px;
    background: var(--rule);
  }
  .contact {
    position: absolute;
    left: 290px;
    top: 58px;
  }
  .person-name {
    font-size: 22px;
    font-weight: 700;
    color: var(--ink);
  }
  .person-title {
    font-size: 13px;
    color: var(--muted);
    margin: 2px 0 12px 6px;
  }
  .contact-list { list-style: none; }
  .contact-list li {
    display: flex;
    align-items: center;
    gap: 10px;
    font-size: 14px;
    color: var(--ink);
    margin-bottom: 6px;
  }
  .contact-list svg { width: 13px; height: 13px; flex: none; }
  .address {
    position: absolute;
    left: 0;
    right: 0;
    bottom: 44px;
    text-align: center;
    font-size: 15px;
    color: var(--ink);
  }
</style>
</head>
<body>

  <section class="card card-front">
    <div class="brand-mark"></div>
    <div class="brand-name">Harrowfield Property Partners</div>
    <div class="front-web">www.hrwpp-example.com</div>
  </section>

  <section class="card card-back">
    <div class="back-logo">
      <div class="brand-mark"></div>
      <div class="brand-name">Harrowfield Property Partners</div>
    </div>
    <div class="divider"></div>
    <div class="contact">
      <div class="person-name">Daniel Marlowe</div>
      <div class="person-title">Manager</div>
      <ul class="contact-list">
        <li>
          <svg viewBox="0 0 24 24" aria-hidden="true"><path fill="#0b2a45" d="M6.6 10.8a15.1 15.1 0 0 0 6.6 6.6l2.2-2.2c.3-.3.7-.4 1-.2 1.1.4 2.3.6 3.6.6.6 0 1 .4 1 1V20c0 .6-.4 1-1 1A17 17 0 0 1 3 4c0-.6.4-1 1-1h3.5c.6 0 1 .4 1 1 0 1.3.2 2.5.6 3.6.1.3 0 .7-.2 1z"/></svg>
          (555) 014-2290
        </li>
        <li>
          <svg viewBox="0 0 24 24" aria-hidden="true"><rect x="2.5" y="5" width="19" height="14" rx="1.5" fill="none" stroke="#0b2a45" stroke-width="2"/><path d="M3 6l9 7 9-7" fill="none" stroke="#0b2a45" stroke-width="2"/></svg>
          info@hrwpp-example.com
        </li>
        <li>
          <svg viewBox="0 0 24 24" aria-hidden="true"><circle cx="12" cy="12" r="9.5" fill="none" stroke="#0b2a45" stroke-width="2"/><ellipse cx="12" cy="12" rx="4" ry="9.5" fill="none" stroke="#0b2a45" stroke-width="1.6"/><path d="M2.5 12h19M4 7h16M4 17h16" stroke="#0b2a45" stroke-width="1.6"/></svg>
          www.hrwpp-example.com
        </li>
      </ul>
    </div>
    <div class="address">480 Meridian Ave, Suite 1402, Fairhaven, FL 33999</div>
  </section>

</body>
</html>
```